Business cards for a naturopathic day clinic for stem cell therapy

We need a basic design for a day clinic, that offers stem cell therapies for Lyme therapy and other severe chronic illnesses.
Our name is "Casa velorìn", which can be translated into "Manor Velorbloom". We are a couple of naturopaths working along side physiotherapists and osteopaths, yoga teachers and massage therapists. I attached our logo.

```html
<!DOCTYPE html>
<html lang="en">
<head>
<meta charset="utf-8">
<title>Casa velorìn – Business Cards</title>
<link href="https://fonts.googleapis.com/css2?family=Montserrat:wght@300;400;700&display=swap" rel="stylesheet">
<style>
  :root {
    --backdrop: #3b312c;
    --card: #1c1c1b;
    --lime: #bcd04d;
    --taupe: #a89587;
    --paper-text: #f2f2ee;
  }
  * { margin: 0; padding: 0; box-sizing: border-box; }
  html, body { width: 1200px; height: 716px; overflow: hidden; }
  body {
    background: var(--backdrop);
    font-family: "Montserrat", sans-serif;
    position: relative;
  }
  .card {
    position: absolute;
    top: 208px;
    width: 540px;
    height: 300px;
    background: var(--card);
    border-bottom: 3px solid var(--lime);
    box-shadow: 0 14px 30px rgba(0,0,0,.45);
    overflow: hidden;
  }
  .card--front { left: 30px; }
  .card--back { left: 630px; }

  .brand {
    display: flex;
    align-items: center;
    gap: 14px;
    color: var(--lime);
    font-weight: 300;
    letter-spacing: .5px;
  }
  .brand__dot {
    border: 2px solid var(--taupe);
    border-radius: 50%;
    flex: none;
  }
  .card--front .brand {
    position: absolute;
    left: 40px;
    top: 110px;
    font-size: 54px;
  }
  .card--front .brand__dot { width: 58px; height: 58px; }

  .card--back .brand {
    position: absolute;
    right: 34px;
    top: 36px;
    font-size: 26px;
    gap: 10px;
  }
  .card--back .brand__dot { width: 28px; height: 28px; }

  .contact {
    position: absolute;
    right: 34px;
    top: 100px;
    text-align: right;
    color: var(--paper-text);
    font-size: 12.5px;
    line-height: 1.5;
  }
  .contact__name {
    color: var(--lime);
    font-weight: 700;
    font-size: 22px;
    letter-spacing: .5px;
    line-height: 1.1;
  }
  .contact__role {
    font-size: 12px;
    letter-spacing: 1px;
    margin-bottom: 8px;
  }
  .contact__line {
    display: flex;
    justify-content: flex-end;
    align-items: center;
    gap: 6px;
  }
  .contact__line svg { width: 11px; height: 11px; flex: none; }
  .edge-tab {
    position: absolute;
    right: 0;
    top: 168px;
    width: 5px;
    height: 34px;
    background: var(--lime);
  }
</style>
</head>
<body>
  <section class="card card--front" aria-label="Card front">
    <div class="brand"><span class="brand__dot"></span><span>Casa velorìn</span></div>
  </section>

  <section class="card card--back" aria-label="Card back">
    <div class="brand"><span class="brand__dot"></span><span>Casa velorìn</span></div>
    <div class="contact">
      <p class="contact__name">JONAS ALBRECHT</p>
      <p class="contact__role">DIRECTOR</p>
      <p>Lindenweg 8,</p>
      <p>61240 Fernau, Germany</p>
      <p class="contact__line">+49 6100 5550142
        <svg viewBox="0 0 12 12"><path d="M3 1l2 2.5-1.2 1.2a6 6 0 0 0 3.5 3.5L8.5 7 11 9l-1.5 2C5 11 1 7 1 2.5z" fill="var(--lime)"/></svg></p>
      <p class="contact__line">06100 5550187
        <svg viewBox="0 0 12 12"><rect x="3" y="1" width="6" height="3" fill="var(--lime)"/><rect x="1" y="4.5" width="10" height="4" rx="1" fill="var(--lime)"/><rect x="3" y="8" width="6" height="3" fill="var(--lime)"/></svg></p>
      <p class="contact__line">info@casa-velorin.de
        <svg viewBox="0 0 12 12"><rect x="1" y="2.5" width="10" height="7" fill="none" stroke="var(--lime)" stroke-width="1.2"/><path d="M1 3l5 4 5-4" fill="none" stroke="var(--lime)" stroke-width="1.2"/></svg></p>
      <p class="contact__line">www.casa-velorin.de
        <svg viewBox="0 0 12 12"><circle cx="6" cy="6" r="5" fill="none" stroke="var(--lime)" stroke-width="1.2"/><ellipse cx="6" cy="6" rx="2" ry="5" fill="none" stroke="var(--lime)"/><path d="M1 6h10" stroke="var(--lime)"/></svg></p>
    </div>
    <span class="edge-tab"></span>
  </section>
</body>
</html>
```